Marketing document for condominium renovation project

Need to have a 6 pages Document to be printed in 11 "x 17" as needed from a google doc.

Use LANDSCAPE orientation.

Team info: https://www.friendwall.example/equipemarcottebelair/

Each page should have a title: ex: Master bedroom

You can combine more than one picture per rooms.

Please use our teem color as per the picture: team colors

Crest Maison Logo: Important, we are a team of real estate agent from the same family. The team is called Marcotte Belair. We work for a real eatate brokerage firm in Canada called Crest maiSon Vecteur.

We need to have both our team logo and crest maiSon logo in each pages.

You could add some pictures that you find apporpriate by walking around in the 3d model:
https://roomwalker.example/360vr/58120397-1844213096

Do some print screen of scene you think appropriate.

Target Market(s)

High end condominium / house buyer

Industry/Entity Type

Real Estate

Font styles to use
Sans Serif

Requirements
Must have
• one of the page should be text summary that includes 3 sections as per follow:
section 1:
- description

section 2
- Room and room dimensions
2 columns describing all rooms

section 3
- budget:
- 10 lines of cost
- 1 line sub total
- 1 line taxes1
- 1 line taxes2
- 1 grand total line
Nice to have
• You could add some pictures that you find appropriate by walking around in the 3d model:

Do some print screen of scene you like.
Should not have
• Too much fancy high end charaters and style.

I want more modern or contemporary

```html
<!DOCTYPE html>
<html lang="en">
<head>
<meta charset="utf-8">
<title>Marcotte Belair – Condominium Renovation Summary</title>
<link href="https://fonts.googleapis.com/css2?family=Montserrat:wght@400;500;600;700&display=swap" rel="stylesheet">
<style>
  :root {
    --backdrop: #e6e6ea;
    --slate: #5d5c67;
    --panel-dark: #2f2e35;
    --panel: #403f47;
    --stripe: #6d6c75;
    --footer: #232227;
    --accent: #e31e2d;
    --ink-light: #ececf0;
    --ink-dark: #1a1a1a;
    --ink-grey: #6a6a70;
    --rule: #4a4950;
    --paper: #ffffff;
  }
  * { margin: 0; padding: 0; box-sizing: border-box; }
  html, body { width: 928px; height: 1200px; overflow: hidden; background: var(--backdrop); }
  body { font-family: "Montserrat", sans-serif; color: var(--ink-light); }

  /* Landscape 17 x 11 sheet */
  .sheet { position: absolute; left: 0; top: 300px; width: 928px; height: 600px; background: var(--paper); overflow: hidden; }

  .content-area { position: absolute; left: 0; top: 0; width: 600px; height: 420px; background: var(--slate); }

  .section-title { font-weight: 600; font-size: 22px; line-height: 26px; color: var(--ink-light); }

  .description { position: absolute; left: 36px; top: 26px; width: 534px; }
  .description p { margin-top: 10px; font-size: 11.5px; line-height: 15px; }

  .rooms { position: absolute; left: 36px; top: 150px; width: 534px; }
  .rooms-columns { display: flex; gap: 24px; margin-top: 12px; }
  .rooms-list { width: 255px; list-style: none; }
  .rooms-list li { font-size: 11px; line-height: 14px; margin-bottom: 8px; }
  .room-name { display: block; font-weight: 600; }

  .budget { position: absolute; left: 600px; top: 0; width: 305px; height: 420px; background: var(--panel); }
  .budget-head { height: 58px; background: var(--panel-dark); padding: 16px 0 0 30px; }
  .budget-table { position: absolute; left: 18px; top: 74px; width: 287px; border-collapse: collapse; }
  .budget-table td { height: 22px; font-size: 11px; padding: 0 0 0 10px; vertical-align: middle; white-space: nowrap; }
  .budget-table td.label { width: 170px; border-right: 2px solid var(--panel); }
  .budget-table td.amount { padding-left: 16px; }
  .budget-table tr.striped td { background: var(--stripe); background-clip: padding-box; border-top: 3px solid var(--panel); border-bottom: 3px solid var(--panel); }
  .budget-table tr.strong td { font-weight: 700; }
  .budget-table tr.total td { height: 30px; font-size: 14px; font-weight: 700; background: var(--stripe); border-top: 6px solid var(--panel); }

  .accent-bar { position: absolute; left: 905px; top: 0; width: 23px; height: 510px; background: var(--accent); }

  .team-footer { position: absolute; left: 0; top: 420px; width: 600px; height: 90px; background: var(--footer); }
  .broker { position: absolute; font-size: 10px; line-height: 13px; font-weight: 500; text-transform: uppercase; color: var(--ink-light); }
  .broker-1 { left: 36px; top: 26px; }
  .broker-2 { left: 222px; top: 26px; }
  .broker-3 { left: 408px; top: 19px; }
  .divider { position: absolute; top: 16px; width: 1px; height: 58px; background: var(--rule); }
  .divider-1 { left: 202px; }
  .divider-2 { left: 388px; }

  .website { position: absolute; left: 600px; top: 420px; width: 305px; height: 90px; line-height: 90px; text-align: center; font-size: 21px; font-weight: 400; color: var(--ink-grey); letter-spacing: 0.3px; }

  .team-mark { position: absolute; left: 36px; top: 526px; display: flex; align-items: center; gap: 12px; }
  .team-mark .square { width: 48px; height: 48px; border: 2px solid #707078; }
  .team-mark .name { font-size: 15px; line-height: 20px; font-weight: 400; color: #707078; text-transform: uppercase; letter-spacing: 0.5px; }

  .brokerage-mark { position: absolute; right: 36px; top: 538px; display: flex; align-items: center; gap: 8px; }
  .brokerage-mark .square { width: 12px; height: 12px; background: var(--ink-dark); }
  .brokerage-mark .name { font-size: 12px; line-height: 15px; font-weight: 700; color: var(--ink-dark); text-transform: uppercase; }
</style>
</head>
<body>
<main class="sheet">
  <div class="content-area"></div>

  <section class="description">
    <h1 class="section-title">Description</h1>
    <p>Fully renovated corner condominium on the 14th floor with open city and river views. This bright 2-bedroom, 2-bathroom unit offers an open-concept living space, a chef-inspired kitchen with quartz counters and integrated appliances, wide-plank oak floors throughout, custom built-in storage and a private terrace. Steps from shops, parks and transit.</p>
  </section>

  <section class="rooms">
    <h2 class="section-title">Room and room dimensions</h2>
    <div class="rooms-columns">
      <ul class="rooms-list">
        <li><span class="room-name">Living room — 18'4" × 15'2"</span>Oak floors, floor-to-ceiling windows</li>
        <li><span class="room-name">Dining room — 12'6" × 11'0"</span>Open to kitchen, pendant lighting</li>
        <li><span class="room-name">Kitchen — 14'2" × 10'8"</span>Quartz island, integrated appliances</li>
        <li><span class="room-name">Entrance hall — 8'0" × 6'4"</span>Custom closet, porcelain tile</li>
        <li><span class="room-name">Terrace — 16'0" × 7'6"</span>South-west exposure, city views</li>
      </ul>
      <ul class="rooms-list">
        <li><span class="room-name">Master bedroom — 15'8" × 13'0"</span>Walk-in closet, blackout blinds</li>
        <li><span class="room-name">Ensuite bath — 10'2" × 8'6"</span>Glass shower, double vanity</li>
        <li><span class="room-name">Second bedroom — 12'4" × 11'2"</span>Built-in desk and wardrobe</li>
        <li><span class="room-name">Bathroom — 8'8" × 6'10"</span>Soaker tub, heated floors</li>
        <li><span class="room-name">Laundry — 6'2" × 5'0"</span>Stacked washer and dryer</li>
      </ul>
    </div>
  </section>

  <section class="budget">
    <div class="budget-head"><h2 class="section-title">Budget</h2></div>
    <table class="budget-table">
      <tr class="striped"><td class="label">Demolition &amp; disposal</td><td class="amount">$6,800</td></tr>
      <tr><td class="label">Flooring</td><td class="amount">$18,450</td></tr>
      <tr class="striped"><td class="label">Kitchen cabinetry</td><td class="amount">$24,900</td></tr>
      <tr><td class="label">Countertops</td><td class="amount">$9,600</td></tr>
      <tr class="striped"><td class="label">Bathroom fixtures</td><td class="amount">$12,300</td></tr>
      <tr><td class="label">Lighting &amp; electrical</td><td class="amount">$7,850</td></tr>
      <tr class="striped"><td class="label">Painting</td><td class="amount">$5,400</td></tr>
      <tr><td class="label">Plumbing</td><td class="amount">$6,750</td></tr>
      <tr class="striped"><td class="label">Windows &amp; doors</td><td class="amount">$11,200</td></tr>
      <tr><td class="label">Design &amp; permits</td><td class="amount">$4,250</td></tr>
      <tr class="striped strong"><td class="label">Sub total</td><td class="amount">$107,500</td></tr>
      <tr class="striped"><td class="label">GST (5%)</td><td class="amount">$5,375</td></tr>
      <tr class="striped"><td class="label">QST (9.975%)</td><td class="amount">$10,723</td></tr>
      <tr class="total"><td class="label">Total</td><td class="amount">$123,598</td></tr>
    </table>
  </section>

  <div class="accent-bar"></div>

  <footer class="team-footer">
    <p class="broker broker-1">Lise Marcotte<br>Real Estate Broker<br>514-555-0143</p>
    <span class="divider divider-1"></span>
    <p class="broker broker-2">Anne Marcotte<br>Real Estate Broker<br>514-555-0178</p>
    <span class="divider divider-2"></span>
    <p class="broker broker-3">Gabrielle Belair<br>Residential Real<br>Estate Broker<br>514-555-0192</p>
  </footer>

  <p class="website">www.lmarcotte.com</p>

  <div class="team-mark">
    <span class="square"></span>
    <span class="name">Marcotte<br>Belair</span>
  </div>

  <div class="brokerage-mark">
    <span class="square"></span>
    <span class="name">Crest maiSon<br>Vecteur</span>
  </div>
</main>
</body>
</html>
```